Building company needs a new logo and letterhead design

We need a new and refreshed logo and letterhead design for an existing building company. We specialise in residential as well as commercial building/construction, design and project management. Our company name is Talvek Constructions Pty Ltd. Our primary colours that we want to use are black/orange/white. We do renovations/alterations/new homes both residential and commercial. We are a medium sized building company. We want something simple and modern.

Industry/Entity Type

Residential

```html
<!DOCTYPE html>
<html lang="en">
<head>
<meta charset="utf-8">
<title>Talvek Constructions Pty Ltd – Letterhead</title>
<link href="https://fonts.googleapis.com/css2?family=Tinos:wght@400;700&display=swap" rel="stylesheet">
<style>
  :root {
    --ink: #111111;
    --orange: #f07a1a;
    --paper: #ffffff;
    --rule: #9a9a9a;
    --machine-dark: #1c1c1c;
  }
  * { margin: 0; padding: 0; box-sizing: border-box; }
  html, body { width: 870px; height: 1200px; overflow: hidden; background: var(--paper); }
  .letterhead {
    position: relative;
    width: 870px;
    height: 1200px;
    background: var(--paper);
    font-family: "Tinos", "Times New Roman", serif;
    color: var(--ink);
  }
  .brand {
    position: absolute;
    left: 36px;
    top: 52px;
  }
  .brand-row {
    display: flex;
    align-items: center;
    gap: 14px;
  }
  .brand-mark {
    width: 22px;
    height: 22px;
    background: var(--orange);
  }
  .brand-name {
    font-weight: 700;
    font-size: 72px;
    line-height: 1;
    color: var(--ink);
  }
  .brand-tagline {
    margin-top: 6px;
    font-size: 22px;
    color: var(--ink);
  }
  .postal-address {
    position: absolute;
    right: 28px;
    top: 95px;
    font-style: normal;
    font-weight: 700;
    font-size: 20px;
    line-height: 1.22;
  }
  .machine-silhouette {
    position: absolute;
    left: 380px;
    top: 960px;
    width: 480px;
    height: 146px;
    background: linear-gradient(180deg, rgba(28,28,28,0) 0%, rgba(28,28,28,0.35) 55%, var(--machine-dark) 100%);
  }
  .ground-rule {
    position: absolute;
    left: 0;
    right: 0;
    top: 1108px;
    height: 2px;
    background: var(--rule);
  }
  .contact-phones,
  .contact-online {
    position: absolute;
    top: 1122px;
    font-size: 20px;
    line-height: 1.28;
  }
  .contact-phones { left: 12px; }
  .contact-online { right: 20px; top: 1148px; text-align: right; }
  .label { color: var(--orange); }
</style>
</head>
<body>
  <div class="letterhead">
    <header class="brand">
      <div class="brand-row">
        <div class="brand-name">Talvek</div>
        <div class="brand-mark"></div>
      </div>
      <div class="brand-tagline">Constructions Pty Ltd.</div>
    </header>

    <address class="postal-address">
      PO Box 512<br>
      Ashbury<br>
      NSW&nbsp; 2193
    </address>

    <div class="machine-silhouette" role="img" aria-label="Black silhouette of an excavator with its arm lowered to the ground"></div>
    <div class="ground-rule"></div>

    <footer>
      <div class="contact-phones">
        <div><span class="label">Tel:</span> 0295550142</div>
        <div><span class="label">Fax:</span> 0295550178</div>
        <div><span class="label">Mobile:</span> 0400555816</div>
      </div>
      <div class="contact-online">
        <div><span class="label">Email:</span> office@talvekmail.com.au</div>
        <div><span class="label">Web:</span> www.talvekconstructions.com.au</div>
      </div>
    </footer>
  </div>
</body>
</html>
```